Chiropractic healthcare group business card

We are a Portland Oregon based chiropractic healthcare group. Looking for a new business card design. Something cutting edge, that shows off our new logo and tag line.Use either of the attached logos.Our tag line = "Who would you be without pain?"I'm open to about anything, impress me!!
Target Market(s)
Chiropractic patients - Auto injury, back pain, sports injuries, neck , shoulder, hip, knee, ankle pain.
Industry/Entity Type
Chiropractic
Contact Information for Business Card
Dr. Bram Holtvick, D.C.
Clinic name - Fernway Chiropractic
2 clinics
location #1
20418 NW Marwick Road
Suite B
North Plains, OR 97133
Location #2
13529 SE Calloway Street
Portland OR 97236
Main phone line 971.555.0143
website : www.FernwayClinics.example
Tag line "Who would you be without pain?"
Colors
Designer to choose colors to be used in the design.
Requirements
Must have
- Use the logo colors -- Want the orange color to be a TRUE orange.
- Both clinic address
- phone number
- website
- personal email - b.holtvick@ReliefBeginsHere.example
- tag line - "Who would you be without pain?"

```html
<!DOCTYPE html>
<html lang="en">
<head>
<meta charset="utf-8">
<title>Fernway Chiropractic – Business Card</title>
<link rel="stylesheet" href="https://fonts.googleapis.com/css2?family=Montserrat:wght@400;500;700;800&family=Open+Sans:wght@700&display=swap">
<style>
  :root {
    --orange: #f7931e;
    --orange-light: #f9a825;
    --orange-deep: #f07f16;
    --ink: #2b2b2b;
    --grey: #6d6e71;
    --white: #ffffff;
    --stage: #e9e9ea;
  }
  * { box-sizing: border-box; margin: 0; padding: 0; }
  html, body { width: 1200px; height: 900px; overflow: hidden; }
  body {
    background: var(--stage);
    font-family: "Montserrat", Arial, sans-serif;
    position: relative;
  }
  .card {
    position: absolute;
    left: 337px;
    width: 525px;
    height: 300px;
    border-radius: 22px;
    overflow: hidden;
    box-shadow: 0 6px 18px rgba(0,0,0,0.12);
  }
  /* Front */
  .card--front { top: 110px; background: var(--white); }
  .brand {
    position: absolute; left: 40px; top: 56px;
    display: flex; align-items: center; gap: 12px;
  }
  .brand__square { width: 28px; height: 28px; background: var(--orange); }
  .brand__name {
    font-weight: 800; font-size: 26px; letter-spacing: 4px; color: var(--ink);
    line-height: 1;
  }
  .brand__sub {
    position: absolute; left: 80px; top: 90px;
    font-size: 10px; letter-spacing: 3px; color: var(--orange); font-weight: 500;
  }
  .contact {
    position: absolute; left: 285px; top: 50px; color: var(--grey);
    font-size: 13px; line-height: 1.45;
  }
  .contact__name { color: var(--ink); font-weight: 700; font-size: 15px; }
  .contact__clinic { margin-bottom: 12px; }
  .address-band {
    position: absolute; left: 0; right: 0; bottom: 0; height: 92px;
    background: linear-gradient(90deg, var(--orange-deep), var(--orange));
    color: var(--white); font-size: 12px; line-height: 1.65;
    padding: 16px 0 0 40px;
  }
  /* Back */
  .card--back {
    top: 480px;
    background: linear-gradient(135deg, var(--orange-deep), var(--orange-light));
  }
  .tagline {
    position: absolute; left: 50%; top: 50%;
    transform: translate(-50%, -50%) rotate(-8deg);
    background: var(--white);
    padding: 12px 30px;
    clip-path: polygon(2% 8%, 30% 0, 70% 6%, 99% 2%, 100% 90%, 72% 100%, 35% 93%, 0 100%);
    font-family: "Open Sans", Arial, sans-serif;
    font-weight: 700; font-size: 21px; color: var(--ink); white-space: nowrap;
  }
</style>
</head>
<body>
  <section class="card card--front">
    <div class="brand">
      <span class="brand__square"></span>
      <span class="brand__name">FERNWAY</span>
    </div>
    <span class="brand__sub">CHIROPRACTIC</span>
    <div class="contact">
      <p class="contact__name">Dr. Bram Holtvick, D.C.</p>
      <p class="contact__clinic">Fernway Chiropractic</p>
      <p>971.555.0143</p>
      <p>www.FernwayClinics.example</p>
    </div>
    <div class="address-band">
      <p>13529 SE Calloway Street, Portland OR 97236</p>
      <p>20418 NW Marwick Road, Suite B, North Plains, OR 97133</p>
      <p>b.holtvick@ReliefBeginsHere.example</p>
    </div>
  </section>

  <section class="card card--back">
    <p class="tagline">“Who would you be without pain?”</p>
  </section>
</body>
</html>
```